Card design for Heating and Cooling company

this is for a heating and cooling company we recently updated our logo and need to update our cards. We attached our logo so you can incorporate it into the card. We specialize in residential and commercial furnace and air condition repairs. Have been in business since 2014.

Phone number 555.284.9137

We need the following phrases
:Repairs, Installations, and maintenance
:Quality work at reasonable prices
:residential/commercial
:Licensed &Insured
:Email Pinegrovehvac47@mailbox-example.com
Name: Teodor K (Ted)
Also on back side I would like my logo with wording :Thank you for your business and refferal

Industry/Entity Type

Hvac

Contact Information for Business Card

:residential/commercial
:Licensed & Insured
Name: Teodor K (Ted)
Number:555.284.9136

Requirements
Must have
• Blue and red colors
Nice to have
• Maybe a pic of a furnace or air conditioner

```html
<!DOCTYPE html>
<html lang="en">
<head>
<meta charset="utf-8">
<title>Pinegrove Heating &amp; Cooling – Business Card</title>
<link rel="stylesheet" href="https://fonts.googleapis.com/css2?family=Roboto:ital,wght@0,400;0,500;0,700;1,400&display=swap">
<style>
  :root {
    --page-bg: #e9e6e1;
    --card-front: #ffffff;
    --card-back: #050505;
    --brand-blue: #1aa3ec;
    --brand-red: #ef2b2b;
    --text-grey: #6b6b6b;
    --text-light: #f4f4f4;
    --card-shadow: 0 14px 30px rgba(0,0,0,0.28);
  }
  * { margin: 0; padding: 0; box-sizing: border-box; }
  html, body {
    width: 1200px; height: 1040px; overflow: hidden;
    background: var(--page-bg);
    font-family: "Roboto", Arial, sans-serif;
  }
  .sheet {
    position: relative; width: 1200px; height: 1040px;
  }
  .card {
    position: absolute; left: 200px; width: 800px; height: 457px;
    box-shadow: var(--card-shadow);
  }
  .card--front { top: 43px; background: var(--card-front); }
  .card--back { top: 540px; background: var(--card-back); color: var(--text-light); }

  /* Front */
  .brand-mark {
    position: absolute; display: flex; align-items: center; gap: 14px;
  }
  .brand-mark__dot {
    width: 30px; height: 30px; border-radius: 50%; background: var(--brand-red);
  }
  .brand-mark__name {
    font-weight: 700; font-size: 46px; letter-spacing: 1px; color: var(--brand-blue);
    text-transform: uppercase;
  }
  .card--front .brand-mark { left: 70px; top: 150px; }
  .owner-name {
    position: absolute; left: 240px; top: 372px;
    font-weight: 500; font-size: 30px; color: var(--brand-blue);
  }
  .contact {
    position: absolute; right: 70px; top: 300px; text-align: left;
    font-size: 17px; line-height: 1.35; color: var(--text-grey);
  }

  /* Back */
  .card--back .brand-mark {
    left: 0; right: 0; top: 70px; justify-content: center;
  }
  .services {
    position: absolute; left: 0; right: 0; top: 175px; text-align: center;
    font-size: 20px; line-height: 1.5;
  }
  .thanks {
    position: absolute; left: 0; right: 0; top: 355px; text-align: center;
    font-style: italic; font-size: 19px;
  }
</style>
</head>
<body>
<main class="sheet">
  <section class="card card--front" aria-label="Card front">
    <div class="brand-mark">
      <span class="brand-mark__dot"></span>
      <span class="brand-mark__name">Pinegrove</span>
    </div>
    <p class="owner-name">Teodor K (Ted)</p>
    <div class="contact">
      <p>Phone. 555.284.9136</p>
      <p>Pinegrovehvac47@mailbox-example.com</p>
      <p>www.pinegrove-example.com</p>
    </div>
  </section>

  <section class="card card--back" aria-label="Card back">
    <div class="brand-mark">
      <span class="brand-mark__dot"></span>
      <span class="brand-mark__name">Pinegrove</span>
    </div>
    <div class="services">
      <p>Repairs, Installations, &amp; maintenance</p>
      <p>Quality work at reasonable prices • Residential/commercial</p>
      <p>Licensed &amp; Insured</p>
    </div>
    <p class="thanks">Thank you for your business &amp; refferal</p>
  </section>
</main>
</body>
</html>
```